Professional and stylish textiles catalogue

Wool throws and cushions product catalogue.
Target audience are business customers (interior stores). Besides providing information about products the catalogue must able to sell, therefore we expect it to be professional and stylish.
Size A5 horizontal.
Content:
1. Cover: Logo and 2011/12 on front, company details on reverse;
2. Page with photo and short info about company;
3. Product pages spread - one item per page. Total 15 double-page spreads;
4. Info page with photo and small text about gift packaging.
Products - throws and cushions. Located as a pair on each spread: throw on the left, cushion on the right. One double-page spread with three throws.
Products mostly are in natural colours: grey, beige and brown. Three throws/cushions in light shades of rose, green and blue.
Comments: catalogue must be in bright colours, could be white with colourful details. Will be great if each product's double-page spread will have stylish details (could be lines) in colours of the product located in this certain double-page spread.
Materials provided:
1. Texts;
2. White background pictures of each product;
3. Several product pictures taken in the interior to use for the cover;
4. Logo.
Complete set of pictures in high resolution will be provided on request.

```html
<!DOCTYPE html>
<html lang="en">
<head>
<meta charset="utf-8">
<title>Lanora 2011/2012 Catalogue Spreads</title>
<link rel="stylesheet" href="https://fonts.googleapis.com/css2?family=EB+Garamond:wght@400;500&display=swap">
<style>
  :root {
    --backdrop: #ece7df;
    --paper: #ffffff;
    --ink: #6b6660;
    --ink-soft: #8b867f;
    --logo-ink: #4f4b47;
    --fold: rgba(0,0,0,0.06);
    --stripe-cream: #f2eee8;
    --stripe-grey: #e5e4e2;
    --stripe-blue: #e7ebef;
    --stripe-beige: #efe7dc;
    --stripe-white: #fafaf9;
    --fabric-light: #d9ccb8;
    --fabric-dark: #c5b398;
    --interior-light: #a9a39b;
    --interior-dark: #3e3934;
    --throw-cream: #ece6dc;
    --product-taupe: #a99c8d;
    --box-grey: #b9b8b6;
    --band: rgba(255,255,255,0.72);
  }
  * { margin: 0; padding: 0; box-sizing: border-box; }
  html, body { width: 1200px; height: 900px; overflow: hidden; }
  body {
    background: var(--backdrop);
    font-family: "EB Garamond", Georgia, serif;
    color: var(--ink);
    position: relative;
  }
  .spread {
    position: absolute;
    left: 220px;
    width: 760px;
    height: 250px;
    display: flex;
    background: var(--paper);
    box-shadow: 0 1px 3px rgba(0,0,0,0.12);
  }
  .spread--cover { top: 28px; }
  .spread--about { top: 320px; }
  .spread--gift  { top: 612px; }
  .spread::after {
    content: "";
    position: absolute;
    left: 379px; top: 0;
    width: 2px; height: 100%;
    background: var(--fold);
  }
  .page {
    position: relative;
    width: 380px;
    height: 250px;
    overflow: hidden;
  }
  .stripes { position: absolute; inset: 0; width: 100%; height: 100%; display: block; }
  .stripes .s-cream { fill: var(--stripe-cream); }
  .stripes .s-grey  { fill: var(--stripe-grey); }
  .stripes .s-blue  { fill: var(--stripe-blue); }
  .stripes .s-beige { fill: var(--stripe-beige); }
  .stripes .s-white { fill: var(--stripe-white); }

  /* Cover */
  .cover-fabric {
    position: absolute; inset: 0;
    background: linear-gradient(135deg, var(--fabric-light), var(--fabric-dark));
  }
  .cover-web {
    position: absolute;
    bottom: 16px; left: 0; width: 100%;
    text-align: center;
    font-size: 6px;
    letter-spacing: 0.5px;
    color: var(--logo-ink);
  }
  .cover-photo {
    position: absolute; inset: 0;
    background: linear-gradient(120deg, var(--interior-light) 0%, var(--throw-cream) 38%, var(--interior-dark) 100%);
  }
  .cover-band {
    position: absolute;
    left: 0; top: 150px;
    width: 100%; height: 52px;
    background: var(--band);
    display: flex;
    align-items: center;
    justify-content: flex-end;
    padding-right: 40px;
    gap: 10px;
  }
  .brand-mark {
    width: 22px; height: 22px;
    background: var(--logo-ink);
  }
  .brand-name {
    font-size: 28px;
    font-weight: 400;
    letter-spacing: 1px;
    color: var(--logo-ink);
  }
  .cover-season {
    position: absolute;
    right: 22px; bottom: 14px;
    font-size: 6px;
    color: var(--paper);
  }

  /* About */
  .about-copy {
    position: absolute;
    left: 34px; top: 30px;
    width: 310px;
    font-size: 6.5px;
    line-height: 1.45;
    color: var(--ink);
  }
  .about-copy p + p { margin-top: 7px; }
  .about-product {
    position: absolute;
    left: 160px; top: 138px;
    width: 180px; height: 90px;
    background: linear-gradient(160deg, var(--product-taupe), #d8cfc4 70%, var(--box-grey));
  }

  /* Gift */
  .gift-copy {
    position: absolute;
    left: 26px; top: 26px;
    width: 200px;
    font-size: 6.5px;
    line-height: 1.45;
  }
  .gift-boxes {
    position: absolute;
    left: 22px; top: 116px;
    width: 336px; height: 112px;
    background: linear-gradient(90deg, #e9e8e6, var(--box-grey) 60%, #d6d5d3);
  }
  .contact-line {
    position: absolute;
    left: 0; bottom: 0;
    width: 100%; height: 26px;
    display: flex;
    align-items: center;
    justify-content: center;
    gap: 8px;
    font-size: 5.5px;
    color: var(--ink-soft);
    background: var(--stripe-white);
  }
</style>
</head>
<body>

<section class="spread spread--cover">
  <div class="page page--back">
    <div class="cover-fabric" role="img" aria-label="Close-up of beige herringbone wool fabric"></div>
    <p class="cover-web">www.lanora.co.uk</p>
  </div>
  <div class="page page--front">
    <div class="cover-photo" role="img" aria-label="Cream fringed wool throw draped over a chair in an interior"></div>
    <div class="cover-band">
      <span class="brand-mark"></span>
      <span class="brand-name">LANORA</span>
    </div>
    <p class="cover-season">2011/2012</p>
  </div>
</section>

<section class="spread spread--about">
  <div class="page page--stripes">
    <svg class="stripes" viewBox="0 0 380 250" preserveAspectRatio="none" aria-hidden="true">
      <rect class="s-white" x="0" y="0" width="380" height="250"/>
      <rect class="s-cream" x="0" y="0" width="22" height="250"/>
      <rect class="s-grey" x="30" y="0" width="8" height="250"/>
      <rect class="s-beige" x="44" y="0" width="26" height="250"/>
      <rect class="s-blue" x="76" y="0" width="14" height="250"/>
      <rect class="s-cream" x="96" y="0" width="30" height="250"/>
      <rect class="s-grey" x="132" y="0" width="6" height="250"/>
      <rect class="s-blue" x="144" y="0" width="20" height="250"/>
      <rect class="s-beige" x="170" y="0" width="12" height="250"/>
      <rect class="s-cream" x="188" y="0" width="28" height="250"/>
      <rect class="s-grey" x="222" y="0" width="10" height="250"/>
      <rect class="s-blue" x="238" y="0" width="24" height="250"/>
      <rect class="s-beige" x="268" y="0" width="8" height="250"/>
      <rect class="s-cream" x="282" y="0" width="22" height="250"/>
      <rect class="s-grey" x="310" y="0" width="14" height="250"/>
      <rect class="s-blue" x="330" y="0" width="10" height="250"/>
      <rect class="s-beige" x="346" y="0" width="20" height="250"/>
    </svg>
  </div>
  <div class="page page--about">
    <div class="about-copy">
      <p>Lanora is a textile design company founded in London in 2010 with the aim of creating high quality, environmentally friendly handwoven throws and cushions.</p>
      <p>Using the finest, long lasting yarns and a harmony of texture and colour, each piece in the Lanora range blends classic design with a fresh, natural and modern feel.</p>
      <p>The 2011/12 collection is made from soft Peruvian baby alpaca, using gentle natural tones, and woven on traditional handlooms by skilled artisans.</p>
    </div>
    <div class="about-product" role="img" aria-label="Folded taupe wool throw with fringe resting on a grey gift box"></div>
  </div>
</section>

<section class="spread spread--gift">
  <div class="page page--gift">
    <p class="gift-copy">Gift wrapped in elegant handmade boxes, Lanora throws and cushions will be a lovely addition to your current collection and are certain to please your valued customers.</p>
    <div class="gift-boxes" role="img" aria-label="Grey handmade gift boxes, one open with a folded throw inside"></div>
  </div>
  <div class="page page--stripes">
    <svg class="stripes" viewBox="0 0 380 250" preserveAspectRatio="none" aria-hidden="true">
      <rect class="s-white" x="0" y="0" width="380" height="250"/>
      <rect class="s-grey" x="6" y="0" width="12" height="250"/>
      <rect class="s-cream" x="24" y="0" width="28" height="250"/>
      <rect class="s-blue" x="58" y="0" width="10" height="250"/>
      <rect class="s-beige" x="74" y="0" width="24" height="250"/>
      <rect class="s-grey" x="104" y="0" width="8" height="250"/>
      <rect class="s-cream" x="118" y="0" width="32" height="250"/>
      <rect class="s-blue" x="156" y="0" width="18" height="250"/>
      <rect class="s-beige" x="180" y="0" width="10" height="250"/>
      <rect class="s-cream" x="196" y="0" width="26" height="250"/>
      <rect class="s-grey" x="228" y="0" width="14" height="250"/>
      <rect class="s-blue" x="248" y="0" width="22" height="250"/>
      <rect class="s-beige" x="276" y="0" width="8" height="250"/>
      <rect class="s-cream" x="290" y="0" width="30" height="250"/>
      <rect class="s-grey" x="326" y="0" width="10" height="250"/>
      <rect class="s-blue" x="342" y="0" width="16" height="250"/>
      <rect class="s-beige" x="364" y="0" width="16" height="250"/>
    </svg>
    <p class="contact-line">
      <span>Lanora Ltd</span><span>|</span>
      <span>48 Mercer Row</span><span>|</span>
      <span>London, EC2 7AB</span><span>|</span>
      <span>+44 (0)20 7946 0381</span>
    </p>
  </div>
</section>

</body>
</html>
```